Florida-based Coastal Landscaping Comapny Needs Postcard Designs

We are a newly established Florida-based, coastal landscaping company that is looking for some really innovative postcards that we can use to get our name our to affluent consumers that live on the coast of Florida (think on the beach) and small to medium sized businesses in the same area. We will be sending out 100s of thousands of these, so need a great design

Target Market(s)

Affluent consumers and small to medium sized businesses

Industry/Entity Type

Landscaping

Font styles to use
Sans Serif

Colors

Designer to choose colors to be used in the design.

Requirements
Must have
• Florida - looking, island looking / paradise, but incorporate landscaping themes
• Need to say something about "Enjoy your yard this summer" or something relating to summer, landscapes and florida
• and would like to make two offers $50.00 off with signing up for one of our routine maintenance programs, or 1 free landscape inspection
Should not have
• Regular generic lawn company designs. We are a top tier landscape design / build plus maintenance firm, so not your mom and pop lawn mowing company

```html
<!DOCTYPE html>
<html lang="en">
<head>
<meta charset="UTF-8">
<title>Shorecrest Summer Postcard</title>
<link rel="stylesheet" href="https://fonts.googleapis.com/css2?family=Lato:wght@300;400;700&family=Roboto+Condensed:ital,wght@0,400;0,700;1,700&display=swap">
<style>
  :root {
    --page-bg: #e9eef2;
    --card-bg: #ffffff;
    --ink: #1c1c1c;
    --teal: #1aa3cc;
    --wave-soft: rgba(150, 200, 236, 0.45);
    --wave-faint: rgba(190, 222, 245, 0.35);
    --sky: #e9f0f2;
    --sea: #b3d3d9;
    --sea-light: #cfe2e4;
    --grass-light: #a6bf52;
    --grass: #8fae3c;
    --grass-deep: #76982c;
    --stamp-line: #d9e3ea;
  }
  * { margin: 0; padding: 0; box-sizing: border-box; }
  html, body { width: 1200px; height: 1200px; overflow: hidden; }
  body { background: var(--page-bg); position: relative; font-family: "Lato", sans-serif; color: var(--ink); }

  .postcard { position: absolute; width: 722px; height: 560px; background: var(--card-bg); overflow: hidden; }
  .postcard--offer { left: 79px; top: 68px; }
  .postcard--front { left: 440px; top: 546px; }

  .offer-backdrop { position: absolute; inset: 0;
    background:
      radial-gradient(ellipse 420px 160px at 560px 90px, var(--wave-soft), rgba(255,255,255,0) 70%),
      radial-gradient(ellipse 300px 120px at 60px 330px, var(--wave-faint), rgba(255,255,255,0) 70%); }

  .brand-name { position: absolute; font-family: "Lato", sans-serif; font-weight: 400; color: var(--teal); letter-spacing: 2px; white-space: nowrap; }
  .postcard--offer .brand-name { left: 53px; top: 48px; font-size: 32px; }
  .postcard--front .brand-name { left: 0; right: 0; padding-left: 56px; text-align: center; top: 72px; font-size: 44px; z-index: 2; }

  .stamp-box { position: absolute; left: 554px; top: 28px; width: 137px; height: 133px; border: 1px solid var(--stamp-line); background: rgba(255,255,255,0.55); }

  .company-intro { position: absolute; left: 33px; top: 106px; width: 500px; font-size: 17.5px; line-height: 21.6px; }

  .offer-block { position: absolute; left: 28px; top: 0; width: 300px; height: 560px; font-family: "Roboto Condensed", sans-serif; }
  .offer-block > * { position: absolute; left: 0; right: 0; text-align: center; }
  .offer-amount { top: 182px; display: flex; justify-content: center; align-items: flex-start; line-height: 1; }
  .offer-amount__currency { font-size: 36px; font-weight: 700; margin-top: 10px; }
  .offer-amount__value { font-size: 94px; font-weight: 700; letter-spacing: -1px; }
  .offer-amount__off { writing-mode: vertical-rl; transform: rotate(180deg); font-size: 27px; font-weight: 400; margin-top: 18px; margin-left: 2px; letter-spacing: 1px; line-height: 1; }
  .offer-terms { top: 274px; font-size: 19.5px; line-height: 24px; }
  .offer-terms em { font-weight: 700; }
  .offer-or { top: 322px; font-size: 18px; line-height: 18px; }
  .offer-free { top: 336px; font-size: 44px; font-weight: 700; line-height: 44px; }
  .offer-free-label { top: 377px; font-size: 19.5px; line-height: 24px; }
  .call-to-action { top: 403px; font-family: "Lato", sans-serif; color: var(--teal); font-size: 29px; line-height: 34px; }
  .contact-line { top: 436px; font-size: 19.5px; line-height: 24px; }

  .front-photo { position: absolute; left: 0; top: 140px; width: 100%; height: 420px;
    background:
      radial-gradient(ellipse 260px 200px at 400px 250px, rgba(255,255,255,0.45), rgba(255,255,255,0) 70%),
      linear-gradient(180deg, #ffffff 0%, var(--sky) 18%, #e2ecef 36%, var(--sea) 40%, var(--sea-light) 56%, var(--grass-light) 62%, var(--grass) 78%, var(--grass-deep) 100%); }

  .front-headline { position: absolute; left: 0; right: 0; top: 324px; text-align: center; font-family: "Lato", sans-serif; font-weight: 300; font-size: 37.5px; letter-spacing: 0.5px; color: var(--ink); }
  .front-call { position: absolute; left: 148px; top: 490px; font-family: "Lato", sans-serif; font-weight: 700; font-size: 38px; color: #000; white-space: nowrap; }
  .front-call span { font-weight: 400; }
</style>
</head>
<body>

  <section class="postcard postcard--offer">
    <div class="offer-backdrop" role="img" aria-label="Soft flowing light blue wave decoration"></div>

    <div class="brand-name">SHORECREST</div>
    <div class="stamp-box"></div>

    <p class="company-intro">We are a top tier landscape design / build plus maintenance firm newly established Florida-based, coastal landscaping company.</p>

    <div class="offer-block">
      <div class="offer-amount">
        <span class="offer-amount__currency">$</span>
        <span class="offer-amount__value">50.00</span>
        <span class="offer-amount__off">OFF</span>
      </div>
      <p class="offer-terms"><em>with signing up</em> for one of our<br>routine maintenance programs,</p>
      <p class="offer-or">or</p>
      <p class="offer-free">1 FREE</p>
      <p class="offer-free-label">LANDSCAPE INSPECTION</p>
      <p class="call-to-action">CALL US NOW</p>
      <p class="contact-line">123456789 / www.yourwebsite.com</p>
    </div>
  </section>

  <section class="postcard postcard--front">
    <div class="front-photo" role="img" aria-label="Photo of two people relaxing with open arms on yoga mats on a seaside lawn"></div>
    <div class="brand-name">SHORECREST</div>
    <h1 class="front-headline">ENJOY YOUR YARD THIS SUMMER</h1>
    <p class="front-call">CALL US NOW <span>123456 789</span></p>
  </section>

</body>
</html>
```